Business Card Design

We have recently seen two business cards that caught our attention and think the designs would work for us. We are an accounting firm that serves small businesses in a variety of industries. Attached are the two business card that inspired us along with very rough layouts. We would like to see a professional layout using our company information.

Industry/Entity Type

Accounting

Contact Information for Business Card

Company Name - Dalworth Pryce
Address - 4180 Brambleton Lane, Suite 310, Houston, TX 77051
713-508-9627 - Main
281-369-0714 - Fax

Team Member Names, emails and phone numbers (see attachment)

```html
<!DOCTYPE html>
<html lang="en">
<head>
<meta charset="utf-8">
<title>Dalworth Pryce – Business Card</title>
<link href="https://fonts.googleapis.com/css2?family=Open+Sans:wght@400;600&display=swap" rel="stylesheet">
<style>
  :root {
    --backdrop: #b4b4b4;
    --card: #ffffff;
    --ink: #111111;
    --muted: #a3a3a3;
    --rule: #000000;
  }
  html, body {
    margin: 0;
    width: 1200px;
    height: 900px;
    overflow: hidden;
    background: var(--backdrop);
    font-family: "Open Sans", Arial, sans-serif;
    color: var(--ink);
  }
  .business-card {
    position: absolute;
    left: 100px;
    top: 165px;
    width: 1000px;
    height: 570px;
    background: var(--card);
    border-radius: 42px;
    overflow: hidden;
  }
  .brand {
    position: absolute;
    left: 0;
    right: 0;
    top: 210px;
    display: flex;
    justify-content: center;
    align-items: center;
    gap: 18px;
  }
  .brand-mark {
    width: 30px;
    height: 30px;
    background: var(--ink);
  }
  .brand-name {
    font-size: 40px;
    font-weight: 600;
    letter-spacing: 3px;
    text-transform: uppercase;
    color: var(--ink);
  }
  .divider-band {
    position: absolute;
    left: 0;
    right: 0;
    top: 330px;
    height: 12px;
    background: var(--rule);
  }
  .contact-person {
    position: absolute;
    right: 490px;
    top: 385px;
    text-align: right;
  }
  .person-name {
    font-size: 27px;
    font-weight: 600;
    margin: 0;
    line-height: 1.2;
  }
  .person-title {
    font-size: 19px;
    color: var(--muted);
    margin: 0 0 22px;
    line-height: 1.3;
  }
  .contact-line {
    font-size: 22px;
    margin: 0;
    line-height: 1.3;
  }
  .column-rule {
    position: absolute;
    left: 540px;
    top: 370px;
    width: 2px;
    height: 160px;
    background: var(--ink);
  }
  .contact-office {
    position: absolute;
    left: 575px;
    top: 380px;
  }
  .office-lines {
    margin: 0 0 18px;
  }
  .office-lines .contact-line {
    font-size: 21px;
  }
  .label {
    display: inline-block;
    width: 62px;
  }
</style>
</head>
<body>
  <div class="business-card">
    <div class="brand">
      <div class="brand-mark"></div>
      <div class="brand-name">Dalworth Pryce</div>
    </div>

    <div class="divider-band"></div>

    <div class="contact-person">
      <p class="person-name">Marisol Thorne</p>
      <p class="person-title">Account Manager</p>
      <p class="contact-line">Direct:&nbsp; 713-557-2049</p>
      <p class="contact-line">Mobile: 832-476-8130</p>
    </div>

    <div class="column-rule"></div>

    <div class="contact-office">
      <div class="office-lines">
        <p class="contact-line"><span class="label">Main:</span>713-508-9627</p>
        <p class="contact-line"><span class="label">Fax:</span>281-369-0714</p>
      </div>
      <div class="office-lines">
        <p class="contact-line">4180 Brambleton Lane, Suite 310</p>
        <p class="contact-line">Houston, TX 77051</p>
      </div>
    </div>
  </div>
</body>
</html>
```